My project benefits Military, First Responders, Police, Fire, and Educators.

Contact Information for Business Card

2 Sided appointment card. Visual side will have my head shot with "Summit Venture" in a bold graffic/text. I am picturing maybe the headshot applied to a filter that has a matrix effect where the picture is made up of data/numbers flowing vertically through the photo. I am of course open to other concepts as well. Side two will have contact info presented in an attractive visual complimenting the front.

```html
<!DOCTYPE html>
<html lang="en">
<head>
<meta charset="UTF-8">
<title>Summit Venture – Appointment Card</title>
<link rel="stylesheet" href="https://fonts.googleapis.com/css2?family=Montserrat:wght@400;700&family=Share+Tech+Mono&display=swap">
<style>
  :root {
    --page-bg: #e6e7e6;
    --ink: #111111;
    --muted: #555555;
    --green: #3fa648;
    --green-light: #6cc04f;
    --green-dark: #2f8e3d;
    --card-white: #ffffff;
    --card-grey: #d9d9d9;
    --black: #050505;
    --matrix-green: #1f7a2c;
  }
  * { margin: 0; padding: 0; box-sizing: border-box; }
  html, body {
    width: 1200px; height: 900px; overflow: hidden;
    background: var(--page-bg);
    font-family: "Montserrat", Arial, sans-serif;
  }
  .canvas { position: relative; width: 1200px; height: 900px; }

  .card {
    position: absolute; left: 320px; width: 560px; height: 320px;
    overflow: hidden; box-shadow: 0 10px 28px rgba(0,0,0,0.25);
  }
  .card svg.card-shapes { position: absolute; inset: 0; }

  /* Visual side */
  .card--visual { top: 100px; background: var(--black); }
  .headshot-matrix {
    position: absolute; left: 0; top: 0; width: 400px; height: 320px;
    background:
      radial-gradient(ellipse at 45% 55%, rgba(5,5,5,0.95) 0 28%, transparent 52%),
      linear-gradient(90deg, #0d3a14 0%, var(--matrix-green) 35%, #0f4a19 70%, var(--black) 100%);
  }
  .brand-vertical {
    position: absolute; top: 160px; left: 495px;
    transform: translate(-50%, -50%) rotate(90deg);
    white-space: nowrap;
    font-family: "Share Tech Mono", "Courier New", monospace;
    font-size: 30px; color: var(--green-light); letter-spacing: 2px;
  }

  /* Contact side */
  .card--contact {
    top: 480px;
    background: linear-gradient(200deg, var(--card-white) 0%, #f1f1f1 55%, var(--card-grey) 100%);
  }
  .brand-band-text {
    position: absolute; left: 95px; top: 160px;
    transform: translate(-50%, -50%) rotate(-90deg);
    white-space: nowrap;
    font-family: "Share Tech Mono", "Courier New", monospace;
    font-size: 30px; color: var(--ink); letter-spacing: 2px;
  }
  .person { position: absolute; left: 262px; right: 12px; top: 86px; }
  .person-line { display: flex; align-items: center; }
  .person-name { font-size: 24px; font-weight: 700; color: var(--ink); line-height: 1; white-space: nowrap; }
  .person-name .surname { color: var(--green); }
  .name-rule {
    flex: 1; height: 2px; margin-left: 8px; margin-top: 4px;
    background: var(--green);
  }
  .person-title { font-size: 10px; color: var(--muted); margin-top: 4px; }
  .contact-list {
    position: absolute; left: 270px; top: 178px; list-style: none;
    font-size: 12.5px; color: var(--ink); line-height: 16px;
  }
  .contact-list li { display: flex; align-items: center; }
  .contact-list .icon { width: 14px; height: 10px; margin-right: 10px; flex: none; }
  .contact-list .indent { padding-left: 24px; }
</style>
</head>
<body>
<main class="canvas">

  <section class="card card--visual" aria-label="Appointment card, visual side">
    <div class="headshot-matrix" role="img" aria-label="Headshot rendered as vertical streams of green matrix data on black"></div>
    <svg class="card-shapes" width="560" height="320" viewBox="0 0 560 320" aria-hidden="true">
      <polygon points="375,150 445,175 445,212" fill="var(--green)"/>
    </svg>
    <div class="brand-vertical">Summit Venture</div>
  </section>

  <section class="card card--contact" aria-label="Appointment card, contact side">
    <svg class="card-shapes" width="560" height="320" viewBox="0 0 560 320" aria-hidden="true">
      <defs>
        <linearGradient id="bandGradient" x1="0" y1="0" x2="0" y2="1">
          <stop offset="0" stop-color="var(--green-light)"/>
          <stop offset="1" stop-color="var(--green-dark)"/>
        </linearGradient>
      </defs>
      <polygon points="200,95 218,95 206,320 168,320" fill="var(--black)"/>
      <polygon points="0,0 212,0 180,320 0,320" fill="url(#bandGradient)"/>
    </svg>
    <div class="brand-band-text">Summit Venture</div>

    <div class="person">
      <div class="person-line">
        <div class="person-name">Daniel <span class="surname">REYES</span></div>
        <div class="name-rule"></div>
      </div>
      <div class="person-title">general manager</div>
    </div>

    <ul class="contact-list">
      <li>
        <svg class="icon" viewBox="0 0 14 10"><path d="M3 1 L5 1 L6 3 L5 4 Q6 6 8 7 L9 6 L11 7 L11 9 Q5 9 3 1 Z" fill="var(--green)"/></svg>
        +00 22 333 44 5
      </li>
      <li>
        <svg class="icon" viewBox="0 0 14 10"><rect x="2" y="2" width="9" height="6" fill="none" stroke="var(--green)" stroke-width="1.2"/><path d="M2 2 L6.5 5.5 L11 2" fill="none" stroke="var(--green)" stroke-width="1.2"/></svg>
        reyes@summitventure.com
      </li>
      <li>
        <svg class="icon" viewBox="0 0 14 10"><circle cx="6.5" cy="5" r="4" fill="none" stroke="var(--green)" stroke-width="1.2"/><line x1="2.5" y1="5" x2="10.5" y2="5" stroke="var(--green)" stroke-width="1"/></svg>
        www.summitventure.com
      </li>
      <li>
        <svg class="icon" viewBox="0 0 14 10"><path d="M6.5 10 L3.5 5 A3 3 0 1 1 9.5 5 Z" fill="var(--green)"/><circle cx="6.5" cy="3.8" r="1.1" fill="#fff"/></svg>
        Harbor Lane 14b
      </li>
      <li class="indent">0047 Ridgeville</li>
    </ul>
  </section>

</main>
</body>
</html>
```